Healthcare technology firm needs business card layout. Logo provided.

We need a business card design for a new healthcare technology company called Kevrimo.com. The logo is already done so that will be used in the design. We assist patients and their families manage their personal health finances. Our initial product is our web site membership that includes educational content on your health benefits, tools, and downloadable forms.

We would like to see designs that use our existing logo or extend the logo in a creative way. Should be very consumer friendly.

```html
<!DOCTYPE html>
<html lang="en">
<head>
<meta charset="utf-8">
<title>Kevrimo.com – Business Card</title>
<link rel="stylesheet" href="https://fonts.googleapis.com/css2?family=Didact+Gothic&display=swap">
<style>
  :root {
    --backdrop: #d9d9d9;
    --card: #ffffff;
    --ink: #3a3a3a;
    --brand-blue: #1f5fa8;
    --brand-green: #3aa54a;
  }
  * { margin: 0; padding: 0; box-sizing: border-box; }
  html, body {
    width: 1200px;
    height: 900px;
    overflow: hidden;
    background: var(--backdrop);
    font-family: "Didact Gothic", sans-serif;
    color: var(--ink);
  }
  .business-card {
    position: absolute;
    left: 100px;
    top: 164px;
    width: 1000px;
    height: 572px;
    background: var(--card);
    box-shadow: 0 10px 30px rgba(0,0,0,0.18);
  }
  .brand {
    position: absolute;
    left: 190px;
    top: 78px;
    display: flex;
    align-items: center;
    gap: 18px;
  }
  .brand-name {
    font-size: 92px;
    line-height: 1;
    color: var(--brand-blue);
    letter-spacing: 2px;
  }
  .brand-dot {
    width: 26px;
    height: 26px;
    border-radius: 50%;
    background: var(--brand-green);
  }
  .holder {
    position: absolute;
    left: 290px;
    top: 232px;
    width: 320px;
    text-align: center;
    font-size: 34px;
    line-height: 1.2;
  }
  .locations {
    position: absolute;
    left: 660px;
    top: 222px;
    font-size: 26px;
    line-height: 1.4;
    list-style: none;
  }
  .contact {
    position: absolute;
    left: 70px;
    top: 372px;
    list-style: none;
    font-size: 30px;
    line-height: 1.45;
  }
  .contact li { display: flex; align-items: center; gap: 18px; }
  .contact svg { width: 20px; height: 20px; fill: var(--brand-green); }
  .tagline {
    position: absolute;
    left: 330px;
    top: 486px;
    font-size: 30px;
    line-height: 1.2;
  }
</style>
</head>
<body>
  <article class="business-card">
    <div class="brand">
      <span class="brand-name">Kevrimo</span>
      <span class="brand-dot"></span>
    </div>

    <div class="holder">
      <p class="holder-name">Dana R. Whitford</p>
      <p class="holder-title">CEO</p>
    </div>

    <ul class="locations">
      <li>Westhollow</li>
      <li>Maple Crossing</li>
      <li>Ridgeport, Avalane</li>
    </ul>

    <ul class="contact">
      <li>
        <svg viewBox="0 0 24 24" aria-label="Phone"><path d="M6.6 10.8a15.1 15.1 0 0 0 6.6 6.6l2.2-2.2a1 1 0 0 1 1-.25 11.4 11.4 0 0 0 3.6.57 1 1 0 0 1 1 1V20a1 1 0 0 1-1 1A17 17 0 0 1 3 4a1 1 0 0 1 1-1h3.5a1 1 0 0 1 1 1c0 1.25.2 2.45.57 3.57a1 1 0 0 1-.25 1z"/></svg>
        <span>555-014-2276</span>
      </li>
      <li>
        <svg viewBox="0 0 24 24" aria-label="Fax"><path d="M7 3h10v5H7zM4 9h16a2 2 0 0 1 2 2v6h-4v4H6v-4H2v-6a2 2 0 0 1 2-2zm4 7v3h8v-3z"/></svg>
        <span>555-017-3390</span>
      </li>
    </ul>

    <p class="tagline">Making your care costs clearer</p>
  </article>
</body>
</html>
```